Bright Fern Custom Homes business card. Double sided. Modern. professional

Bright Fern Custom Homes
contemporary modern design with our logo /
Double sided with all our contact information
Use same Green colors as in our Logo. Contemporary logo that grabs your attention. Visually pleasing and balanced. Easy to read, and Vibrant. Would love an option for rounded edges. Embossed logo would be amazing.
Contact Information for Business Card
Dana Welk Owner / General Contractor Bright Fern Custom Homes p: 704.552.1830 m: 912.648.2071 e: brightferncustomhomes@mailbox.example w: www.brightferncustomhomes.example 218 Pryor Meadow Lane Alder Creek, TN 37841

```html
<!DOCTYPE html>
<html lang="en">
<head>
<meta charset="utf-8">
<title>Bright Fern Custom Homes – Business Card</title>
<link rel="stylesheet" href="https://fonts.googleapis.com/css2?family=Marcellus&family=Poppins:wght@400;600&display=swap">
<style>
  :root {
    --backdrop: #0f1a33;
    --fern-green: #6b8434;
    --fern-deep: #4f6a26;
    --card-white: #f2f2f0;
    --ink: #1c1c1c;
    --paper-light: #ffffff;
  }
  * { margin: 0; padding: 0; box-sizing: border-box; }
  html, body { width: 1200px; height: 958px; overflow: hidden; }
  body {
    background: var(--backdrop);
    position: relative;
    font-family: "Poppins", sans-serif;
  }
  .card {
    position: absolute;
    left: 250px;
    width: 700px;
    height: 400px;
    border-radius: 14px;
    overflow: hidden;
  }
  .card-front { top: 50px; background: var(--fern-green); }
  .card-back  { top: 508px; background: var(--card-white); }

  /* front */
  .front-mark {
    position: absolute;
    left: 0; right: 0; top: 86px;
    display: flex; flex-direction: column; align-items: center;
  }
  .brand-dot {
    width: 128px; height: 128px;
    border-radius: 50%;
    background: var(--paper-light);
  }
  .brand-name {
    font-family: "Marcellus", serif;
    font-weight: 400;
    letter-spacing: 0.08em;
    text-transform: uppercase;
    white-space: nowrap;
  }
  .front-mark .brand-name {
    margin-top: 34px;
    font-size: 34px;
    color: var(--paper-light);
  }

  /* back */
  .back-brand {
    position: absolute;
    left: 18px; top: 112px; width: 290px;
    display: flex; flex-direction: column; align-items: center;
  }
  .back-brand .brand-dot {
    width: 78px; height: 78px;
    background: var(--fern-deep);
  }
  .back-brand .brand-name {
    margin-top: 18px;
    font-size: 15px;
    letter-spacing: 0.05em;
    text-align: center;
    color: var(--fern-green);
  }
  .divider {
    position: absolute;
    left: 318px; top: 88px;
    width: 2px; height: 190px;
    background: linear-gradient(to bottom, transparent, var(--fern-green), transparent);
  }
  .contact {
    position: absolute;
    left: 346px; top: 98px;
  }
  .person-name {
    font-family: "Marcellus", serif;
    font-weight: 400;
    font-size: 30px;
    letter-spacing: 0.04em;
    text-transform: uppercase;
    color: var(--ink);
    line-height: 1;
  }
  .person-role {
    margin-top: 6px;
    font-size: 14px;
    color: var(--fern-green);
  }
  .contact-list { list-style: none; margin-top: 22px; }
  .contact-list li {
    display: flex; align-items: center; gap: 9px;
    font-size: 13.5px; color: var(--ink);
    line-height: 1.65;
  }
  .contact-list svg { width: 12px; height: 12px; fill: var(--fern-green); flex: none; }
  .address {
    position: absolute;
    left: 0; right: 0; bottom: 40px;
    text-align: center;
    font-weight: 600;
  }
  .address-company { font-size: 15px; color: var(--fern-green); }
  .address-line { font-size: 12px; color: var(--ink); }
</style>
</head>
<body>

<section class="card card-front" aria-label="Card front">
  <div class="front-mark">
    <div class="brand-dot"></div>
    <p class="brand-name">Bright Fern Custom Homes</p>
  </div>
</section>

<section class="card card-back" aria-label="Card back">
  <div class="back-brand">
    <div class="brand-dot"></div>
    <p class="brand-name">Bright Fern Custom Homes</p>
  </div>

  <div class="divider"></div>

  <div class="contact">
    <h1 class="person-name">Dana Welk</h1>
    <p class="person-role">Owner / General Contractor</p>
    <ul class="contact-list">
      <li>
        <svg viewBox="0 0 24 24"><path d="M6.6 10.8a15.1 15.1 0 0 0 6.6 6.6l2.2-2.2a1 1 0 0 1 1-.25 11.4 11.4 0 0 0 3.6.57 1 1 0 0 1 1 1V20a1 1 0 0 1-1 1A17 17 0 0 1 3 4a1 1 0 0 1 1-1h3.5a1 1 0 0 1 1 1c0 1.25.2 2.45.57 3.6a1 1 0 0 1-.25 1z"/></svg>
        704.552.1830
      </li>
      <li>
        <svg viewBox="0 0 24 24"><path d="M6.6 10.8a15.1 15.1 0 0 0 6.6 6.6l2.2-2.2a1 1 0 0 1 1-.25 11.4 11.4 0 0 0 3.6.57 1 1 0 0 1 1 1V20a1 1 0 0 1-1 1A17 17 0 0 1 3 4a1 1 0 0 1 1-1h3.5a1 1 0 0 1 1 1c0 1.25.2 2.45.57 3.6a1 1 0 0 1-.25 1z"/></svg>
        912.648.2071
      </li>
      <li>
        <svg viewBox="0 0 24 24"><path d="M2 5h20v14H2z M4 7v.5l8 5 8-5V7l-8 5z" fill-rule="evenodd"/></svg>
        brightferncustomhomes@mailbox.example
      </li>
    </ul>
  </div>

  <div class="address">
    <p class="address-company">Bright Fern Custom Homes</p>
    <p class="address-line">218 Pryor Meadow Lane Alder Creek, TN 37841</p>
  </div>
</section>

</body>
</html>
```